BRAMWELL LODGE FISH BAR

We need a flyer design for our fish and chip shop, we are looking for something bright and eye catching with some images possibly in the theme of the ocean but interested in other ideas.
we need the flyer to include the following information;
address- 27-29 the orchard row
Ashcombe Vale
0x42 7rd
phone number 01634 582017
opening hours - Thursday,friday,saturday lunchtimes 12-2pm

Tuesday,wednesday,thursday evenings 4.30-9pm

Friday, Saturday evenings 4.30-9.30pm

card payments excepted.

traditional fish and chips
Aberdeen angus chargrilled steak burgers (free range, organic meat)
kebabs (donner and chicken)

Pension day every Thursday, 50p off any meal deal

special offer,
£1 off large fish and chips with this leaflet

• we would like some images, possibly with an ocean theme but other interested in other ideas to do with fish and chips.

```html
<!DOCTYPE html>
<html lang="en">
<head>
<meta charset="utf-8">
<title>Bramwell Lodge Fish Bar – Flyer</title>
<link rel="stylesheet" href="https://fonts.googleapis.com/css2?family=Kaushan+Script&family=Roboto+Condensed:wght@400;700&family=Oswald:wght@600;700&display=swap">
<style>
  :root{
    --sky-top:#1d5fae;
    --sky-deep:#0f3f86;
    --sea:#2c8fd0;
    --panel:rgba(34,40,92,0.82);
    --offer-red:#e0242b;
    --offer-dark:#9d1418;
    --yellow:#f7c520;
    --orange:#f0a01c;
    --brown:#6b3518;
    --badge-gold:#f4b43a;
    --white:#ffffff;
    --batter:#d88a2e;
    --wood:#b9834a;
  }
  *{box-sizing:border-box;margin:0;padding:0}
  html,body{width:1200px;height:1000px;overflow:hidden;background:#fff}
  .flyer{
    position:absolute;left:139px;top:141px;width:924px;height:718px;
    transform:rotate(-90deg);overflow:hidden;
    font-family:"Roboto Condensed",Arial,sans-serif;color:var(--white);
  }
  .backdrop{
    position:absolute;inset:0;
    background:
      radial-gradient(ellipse 380px 260px at 680px 60px,rgba(61,90,52,.85),rgba(61,90,52,0) 70%),
      radial-gradient(ellipse 260px 200px at 60px 40px,rgba(61,90,52,.55),rgba(61,90,52,0) 70%),
      linear-gradient(180deg,var(--sky-top) 0%,var(--sky-deep) 45%,var(--sea) 85%,#7fb6d8 100%);
  }
  .food-photo{
    position:absolute;left:342px;top:298px;width:582px;height:360px;
    background:
      radial-gradient(ellipse 300px 150px at 300px 110px,var(--batter),rgba(216,138,46,0) 80%),
      radial-gradient(ellipse 340px 200px at 320px 160px,#f4f0e6,rgba(244,240,230,0) 85%),
      linear-gradient(160deg,rgba(185,131,74,0) 30%,var(--wood) 80%);
    border-radius:40px 0 0 0;
  }
  .name{
    position:absolute;left:390px;top:60px;width:500px;text-align:center;
    font-family:"Roboto Condensed",Arial,sans-serif;font-weight:700;
    font-size:64px;line-height:1.05;color:var(--white);letter-spacing:2px;
  }
  .offer{position:absolute;left:22px;top:53px;width:345px;height:145px}
  .offer svg{position:absolute;inset:0}
  .offer-title{position:absolute;left:20px;top:6px;font-family:"Oswald",sans-serif;font-weight:600;font-size:34px;line-height:1}
  .offer-amount{position:absolute;left:18px;top:40px;font-family:"Oswald",sans-serif;font-weight:700;font-size:74px;line-height:1;color:var(--yellow)}
  .offer-note{position:absolute;left:20px;top:124px;font-size:11px;font-weight:700;white-space:nowrap}
  .info{position:absolute;left:0;top:253px;width:377px;height:405px;background:var(--panel);padding:14px 22px}
  .menu{list-style:none;font-size:18px;line-height:1.4}
  .menu li::before{content:"• "}
  .menu b{font-weight:700}
  .rule{height:1px;background:rgba(255,255,255,.7);margin:14px 0;width:310px}
  .hours-title{font-weight:700;font-size:19px;margin-bottom:6px}
  .hours p{font-size:15px;line-height:1.2;margin-bottom:9px}
  .cards{font-weight:700;font-size:18px;line-height:1.1}
  .badge{position:absolute;left:242px;top:483px;width:150px;height:150px}
  .badge-text{position:absolute;inset:0;display:flex;flex-direction:column;align-items:center;justify-content:center;color:var(--brown);text-align:center}
  .badge-script{font-family:"Kaushan Script",cursive;font-size:17px}
  .badge-sub{font-size:8px;font-weight:700;letter-spacing:.5px}
  .badge-amount{font-family:"Oswald",sans-serif;font-weight:700;font-size:31px;color:var(--white);background:var(--brown);width:128px;line-height:1.15}
  .badge-deal{font-family:"Kaushan Script",cursive;font-size:15px}
  .contact-band{position:absolute;left:0;top:658px;width:924px;height:60px;background:var(--orange);display:flex;align-items:center;justify-content:space-between;padding:0 20px 0 12px;font-weight:700;font-size:23px}
  .contact-item{display:flex;align-items:center;gap:8px}
  .contact-item svg{width:18px;height:18px;fill:var(--white)}
</style>
</head>
<body>
<main class="flyer">
  <div class="backdrop" role="img" aria-label="Tropical beach scene with palm leaves, blue sky and sea"></div>
  <div class="food-photo" role="img" aria-label="Battered fish fillets with chips, lemon wedges and parsley on a white plate"></div>

  <header class="name">BRAMWELL LODGE<br>FISH BAR</header>

  <section class="offer">
    <svg viewBox="0 0 345 145" preserveAspectRatio="none">
      <defs><linearGradient id="offerFill" x1="0" y1="0" x2="0" y2="1"><stop offset="0" stop-color="#e0242b"/><stop offset="1" stop-color="#9d1418"/></linearGradient></defs>
      <polygon points="0,0 310,0 345,145 0,145" fill="url(#offerFill)"/>
    </svg>
    <div class="offer-title">Special Offer</div>
    <div class="offer-amount">£1OFF</div>
    <div class="offer-note">large fish and chips with this leaflet Offer</div>
  </section>

  <section class="info">
    <ul class="menu">
      <li><b>Traditional Fish and Chips</b></li>
      <li><b>Aberdeen angus chargrilled<br>&nbsp;&nbsp;steak burgers</b> (free range, organic meat)</li>
      <li><b>Kebabs</b> (donner and chicken)</li>
    </ul>
    <div class="rule"></div>
    <div class="hours">
      <div class="hours-title">Opening Hours</div>
      <p>Thursday, friday, saturday<br>lunch times 12-2pm</p>
      <p>Tuesday, wednesday, thursday<br>evenings 4.30-9pm</p>
      <p>Friday, Saturday<br>evenings 4.30-9.30pm</p>
    </div>
    <div class="rule"></div>
    <div class="cards">Card Payments<br>accepted.</div>
  </section>

  <aside class="badge">
    <svg viewBox="0 0 150 150" width="150" height="150">
      <circle cx="75" cy="75" r="74" fill="#6b3518"/>
      <circle cx="75" cy="75" r="66" fill="#f4b43a"/>
    </svg>
    <div class="badge-text">
      <div class="badge-sub">★ ★ ★</div>
      <div class="badge-script">Pensioners Day</div>
      <div class="badge-sub">EVERY THURSDAY</div>
      <div class="badge-amount">50p OFF</div>
      <div class="badge-deal">any meal deal</div>
      <div class="badge-sub">★ ★ ★</div>
    </div>
  </aside>

  <footer class="contact-band">
    <div class="contact-item">
      <svg viewBox="0 0 24 24"><path d="M6.6 10.8a15.1 15.1 0 0 0 6.6 6.6l2.2-2.2a1 1 0 0 1 1-.25 11.4 11.4 0 0 0 3.6.57 1 1 0 0 1 1 1V20a1 1 0 0 1-1 1A17 17 0 0 1 3 4a1 1 0 0 1 1-1h3.5a1 1 0 0 1 1 1c0 1.25.2 2.45.57 3.57a1 1 0 0 1-.25 1z"/></svg>
      <span>01634 582017</span>
    </div>
    <div class="contact-item">
      <svg viewBox="0 0 24 24"><path d="M12 2a7 7 0 0 0-7 7c0 5.25 7 13 7 13s7-7.75 7-13a7 7 0 0 0-7-7zm0 9.5A2.5 2.5 0 1 1 12 6.5a2.5 2.5 0 0 1 0 5z"/></svg>
      <span>27-29 The Orchard Row Ashcombe Vale</span>
    </div>
  </footer>
</main>
</body>
</html>
```